依頼詳細
創業して初めて出す年賀状です。教育委員会や学校の先生、保護者、地域の方など多様な方へ、日頃の御礼と、来年以降の事業への期待を抱いて頂けるようなデザインを希望します。
2色で印刷します。「メイン色:DIC897(青)」、「サブ:おまかせ」の2色を使ったデザインをご提案下さい。
記載項目
1、挨拶文
①Raise up now!
Aim So High We'll Never Be Bored.

②創業して初めての新年を迎えることができました
ひとえに皆々様のご支援の賜物と感謝いたしております
本年も何卒よろしくお願い申し上げます

③Have a great New Year! 2015

それぞれ次の役割をふまえてデザイン下さい。
①はキャッチ、②は小さく、③は適当に。

2、基本情報
(社名)一般社団法人若葉学習協働センター
(代表者名)代表理事 野村 拓

(住所)〒604-0937 京都府京都市中京区竹屋町通柳馬場東入桔梗町218 藤田ビル305
(電話)075-382-9127
(FAX)075-382-9128
希望イメージ
• シンプル
複雑
• 単色
カラフル
• 暗い
明るい
• 日常
高級
• 遊び心
厳粛
• 未来的
伝統的
• 女性的
男性的
希望する色
青系、「メイン色:DIC897(青)」、「サブ:おまかせ」の2色を使って下さい
納品ファイル
• 高解像度JPG (.jpg)
• イラストレーター形式 (.ai)
補足説明
弊団体のロゴデータをお渡ししますので、ロゴを活かしてデザインをご提案下さい
依頼公開後の追記内容
■ 選んだ理由

複数の要素がある中で、当方の依頼意図を汲んで強弱を付けて下さったことが大きな理由です。

■ 提案者全員のお礼・コメント

このたびは多数のご提案を頂戴しまして、誠にありがとうございました。

初めてワークモールを利用しましたが、同じオーダーでここまでバリエーションが出ると想像もしておりませんでした。イラスト作成など個性を活かしたご提案についても御礼申し上げます。

今後ともどうぞよろしくお願い致します。

```html
<!DOCTYPE html>
<html lang="ja">
<head>
<meta charset="utf-8">
<title>年賀状 2015 — 若葉学習協働センター</title>
<link rel="stylesheet" href="https://fonts.googleapis.com/css2?family=Oswald:wght@700&family=Roboto+Condensed:wght@700&family=Noto+Sans+JP:wght@400;700;900&display=swap">
<style>
  :root {
    --navy: #2e4a78;
    --navy-deep: #24406e;
    --paper: #e9ebf2;
    --stripe: #d3d8e4;
    --wave-light: #7f97bd;
    --white: #ffffff;
  }
  * { margin: 0; padding: 0; box-sizing: border-box; }
  html, body { width: 813px; height: 1200px; overflow: hidden; background: var(--paper); }
  .card {
    position: relative;
    width: 813px;
    height: 1200px;
    background: var(--paper);
    overflow: hidden;
    font-family: "Noto Sans JP", sans-serif;
    color: var(--navy);
  }
  .header-band { position: absolute; left: 0; top: 0; width: 813px; height: 320px; }
  .catch {
    position: absolute;
    left: 22px;
    top: 118px;
    font-family: "Oswald", sans-serif;
    font-weight: 700;
    font-size: 112px;
    line-height: 1;
    color: var(--white);
    letter-spacing: 0;
    transform: rotate(-10deg);
    transform-origin: left bottom;
    white-space: nowrap;
  }
  .motto {
    position: absolute;
    top: 274px;
    width: 100%;
    text-align: center;
    font-family: "Roboto Condensed", sans-serif;
    font-weight: 700;
    font-size: 42px;
    line-height: 1.12;
    color: var(--navy);
  }
  .greeting {
    position: absolute;
    top: 402px;
    width: 100%;
    text-align: center;
    font-weight: 700;
    font-size: 19px;
    line-height: 1.7;
    color: var(--navy);
  }
  .emblem-art {
    position: absolute;
    left: 40px;
    top: 528px;
    width: 740px;
    height: 515px;
    border-radius: 50%;
    background: radial-gradient(ellipse at 50% 50%, var(--navy) 0%, var(--navy) 90%, var(--wave-light) 96%, rgba(233,235,242,0) 100%);
  }
  .new-year {
    position: absolute;
    left: 452px;
    top: 968px;
    font-family: "Roboto Condensed", sans-serif;
    font-weight: 700;
    font-size: 24px;
    line-height: 1;
    color: var(--white);
    transform: rotate(-30deg);
    transform-origin: left bottom;
    white-space: nowrap;
  }
  .sender {
    position: absolute;
    top: 1060px;
    width: 100%;
    text-align: center;
    color: var(--navy);
  }
  .sender .org { font-size: 24px; font-weight: 900; line-height: 1.3; }
  .sender .org-type { font-size: 13px; font-weight: 700; margin-right: 6px; }
  .sender .rep { font-size: 13px; font-weight: 700; line-height: 1.4; }
  .sender .rep-name { font-size: 18px; font-weight: 900; margin-left: 6px; }
  .sender .address, .sender .contact { font-size: 15px; font-weight: 400; line-height: 1.55; }
  .sender .address { margin-top: 6px; }
</style>
</head>
<body>
<main class="card">
  <svg class="header-band" viewBox="0 0 813 320" aria-hidden="true">
    <polygon points="0,0 813,0 813,160 0,312" fill="var(--stripe)"/>
    <polygon points="0,0 813,0 813,138 0,292" fill="var(--navy-deep)"/>
  </svg>
  <h1 class="catch">Raise up now!</h1>

  <p class="motto">Ain SO High<br>We'll Never Be Bored.</p>

  <p class="greeting">
    創業して初めての新年を迎えることができました。<br>
    ひとえに皆々様のご支援の賜物と感謝いたしております。<br>
    本年も何卒よろしくお願い申し上げます。
  </p>

  <div class="emblem-art" role="img" aria-label="渦巻く波の円の中に帆船を描いた紺色のイラスト"></div>

  <p class="new-year">Have a great New Year! 2015</p>

  <footer class="sender">
    <p class="org"><span class="org-type">一般社団法人</span>若葉学習協働センター</p>
    <p class="rep">代表理事<span class="rep-name">野村 拓</span></p>
    <p class="address">〒604-0937 京都府京都市中京区竹屋町通柳馬場東入桔梗町218 藤田ビル305</p>
    <p class="contact">TEL 075-382-9127　FAX 075-382-9128</p>
  </footer>
</main>
</body>
</html>
```